Feminine colorfull packaging for coconut skin care brand

We need a design that can be used on different types of packaging for beauty products likes creams, oils, etc.
The products that we will launch will be made with one key ingredient of coconut oil + other added ingredients depending on the type of product. The entire marketing will therefore be based on COCONUTS, palmtrees, sand, beach, bronzing on the beach, holiday feeling, nature, femininity, etc. = A Lifestyle brand with a tropical vibe.
Packaging can be a pot for creams, flaskes for lotions, smaller bottles for oils, etc. Mostly the standard packaging used for beauty products.
We would like to use the color pink ( this can be bright or pastel or any tone of pink) to address the feminine side of our product and a tone of blue-green ( pastel, bright or any tone of this color) to accentuate the use of coconut.
Third would be the color white (this can be added through an accent somewhere on the packaging or this can be the brand name that is written in white)
Lastely we would like the packaging to be light, fresh and playfull. Please feel free to use different colors or shapes ( we do not yet have a logo. This can then be designed followed on the packaging)
The design will be printed on plastic packaging. We are open to very creative designs. We are looking for packaging that catches the eye by its design and/or colors, that is different than others, that distinguishes the product because of its packaging design.
Target Market(s)
Women between 20 - 35 years
Industry/Entity Type
Beauty
Colors
Designer to choose colors to be used in the design.
Look and feel

```html
<!DOCTYPE html>
<html lang="en">
<head>
<meta charset="utf-8">
<title>Coralune Moisturizer Packaging</title>
<link rel="stylesheet" href="https://fonts.googleapis.com/css2?family=Josefin+Sans:wght@600;700&display=swap">
<style>
  :root {
    --backdrop: #f1efe8;
    --lagoon: #0b9a9c;
    --lagoon-light: #25b5b6;
    --hibiscus: #f27bb0;
    --cocoa-leaf: #a8484c;
    --sunny-leaf: #f3e27a;
    --mint-text: #6fe3c4;
    --white: #ffffff;
  }
  * { margin: 0; padding: 0; box-sizing: border-box; }
  html, body {
    width: 1200px;
    height: 960px;
    overflow: hidden;
    background: var(--backdrop);
    font-family: "Josefin Sans", sans-serif;
  }
  .canvas {
    position: relative;
    width: 1200px;
    height: 960px;
  }
  .tropical-print {
    background:
      radial-gradient(circle at 30% 20%, var(--sunny-leaf) 0 8%, transparent 18%),
      radial-gradient(circle at 75% 55%, var(--cocoa-leaf) 0 6%, transparent 20%),
      radial-gradient(circle at 20% 70%, var(--sunny-leaf) 0 5%, transparent 14%),
      linear-gradient(160deg, var(--hibiscus) 0%, var(--lagoon) 45%, var(--hibiscus) 70%, var(--cocoa-leaf) 100%);
  }
  .carton-front {
    position: absolute;
    left: 328px;
    top: 202px;
    width: 284px;
    height: 556px;
  }
  .product-label {
    position: absolute;
    background: var(--lagoon);
    color: var(--white);
    text-align: center;
    display: flex;
    flex-direction: column;
    align-items: center;
    justify-content: center;
  }
  .carton-front .product-label {
    left: 59px;
    top: 119px;
    width: 172px;
    height: 114px;
  }
  .brand-name {
    font-weight: 700;
    color: var(--white);
    line-height: 1;
  }
  .product-type {
    font-weight: 600;
    color: var(--mint-text);
    letter-spacing: 0.18em;
    line-height: 1;
  }
  .ingredient-note {
    font-weight: 700;
    color: var(--white);
    letter-spacing: 0.16em;
    line-height: 1;
  }
  .carton-front .brand-name { font-size: 24px; margin-bottom: 14px; }
  .carton-front .product-type { font-size: 15px; margin-bottom: 14px; }
  .carton-front .ingredient-note { font-size: 7.5px; }

  .tube {
    position: absolute;
    left: 706px;
    top: 213px;
    width: 208px;
    height: 544px;
  }
  .tube-body {
    position: absolute;
    left: 0;
    top: 0;
    width: 208px;
    height: 466px;
    clip-path: polygon(0 0, 100% 0, 80% 100%, 20% 100%);
  }
  .tube .product-label {
    left: 41px;
    top: 90px;
    width: 128px;
    height: 88px;
  }
  .tube .brand-name { font-size: 17px; margin-bottom: 12px; }
  .tube .product-type { font-size: 10px; margin-bottom: 10px; }
  .tube .ingredient-note { font-size: 5px; }
  .tube-cap {
    position: absolute;
    left: 41px;
    top: 466px;
    width: 126px;
    height: 78px;
    background: linear-gradient(90deg, var(--lagoon) 0%, var(--lagoon-light) 50%, var(--lagoon) 100%);
    border-radius: 0 0 63px 63px / 0 0 10px 10px;
  }
</style>
</head>
<body>
  <main class="canvas">
    <section class="carton-front">
      <div class="tropical-print" role="img" aria-label="Tropical pattern of pink, maroon and yellow palm and jungle leaves on a teal ground" style="position:absolute;inset:0;"></div>
      <div class="product-label">
        <p class="brand-name">Coralune</p>
        <p class="product-type">MOISTURIZER</p>
        <p class="ingredient-note">MADE WITH COCONUT OIL</p>
      </div>
    </section>

    <section class="tube">
      <div class="tube-body tropical-print" role="img" aria-label="Tube wrapped in the tropical pink, maroon and yellow leaf pattern on teal"></div>
      <div class="product-label">
        <p class="brand-name">Coralune</p>
        <p class="product-type">MOISTURIZER</p>
        <p class="ingredient-note">MADE WITH COCONUT OIL</p>
      </div>
      <div class="tube-cap"></div>
    </section>
  </main>
</body>
</html>
```